PSD for Magento Site (No Code Required)

I Need 10 pages design for a new Plus-Size Lingerie Site. The site has to be a edgy, fun & clean.

I will need versions of each page for mobile, tablet sizes as well. We are trying to be a new kind of lingerie site. something non traditional. A Fun place to show. Big images, Easy Navigation, Simple Layout.

Full Brief is Attached.

Target Market(s)

Plus size Women, Lingerie Enthusiasts

Industry/Entity Type

Retail

Number of Pages Required

5+ page

Font styles to use
Sans Serif

Colors
000000
ffffff
d3d3d3

Requirements
Must have
• Well Structured Mobile versions of each page
Should not have
• clutter

```html
<!DOCTYPE html>
<html lang="en">
<head>
<meta charset="utf-8">
<title>Lushline – Fringe Black Chemise</title>
<link href="https://fonts.googleapis.com/css2?family=Montserrat:wght@300;400;600;700&family=Great+Vibes&display=swap" rel="stylesheet">
<style>
:root{
  --ink:#231f20;
  --ink-soft:#3a3637;
  --paper:#ffffff;
  --grey:#999999;
  --line:#d3d3d3;
  --text:#1c1c1c;
  --red:#e0474c;
  --blue:#3c4ce8;
  --peach:#f7b77c;
  --photo-a:#eeeeee;
  --photo-b:#cfcfcf;
  --promo-a:#0f1520;
  --promo-b:#2c3344;
}
*{box-sizing:border-box;margin:0;padding:0}
html,body{width:1200px;height:2362px;overflow:hidden;background:var(--paper)}
body{position:relative;font-family:"Montserrat",sans-serif;color:var(--text)}
.abs{position:absolute}
.header{left:0;top:0;width:1200px;height:110px;background:var(--ink)}
.brand{left:47px;top:24px;color:var(--paper);font-size:42px;font-weight:600;letter-spacing:2px;display:flex;align-items:center;gap:14px}
.brand-dot{width:22px;height:22px;border-radius:50%;background:var(--paper)}
.top-link{top:44px;color:var(--paper);font-size:13px;font-weight:600}
.search{left:683px;top:27px;width:246px;height:47px;background:var(--paper);color:#bbb;font-size:12px;padding:16px 12px}
.bag{left:1044px;top:0;width:103px;height:110px;background:var(--ink-soft);color:var(--paper);font-size:13px;font-weight:600;display:flex;align-items:center;justify-content:center;gap:8px}
.mini-bag{left:913px;top:110px;width:234px;height:277px;background:var(--paper);border:1px solid var(--ink);z-index:5;padding:16px 12px}
.mini-bag .thumb{position:absolute;left:12px;top:18px;width:60px;height:126px;background:linear-gradient(var(--photo-a),var(--photo-b))}
.mini-bag .info{position:absolute;left:82px;top:20px;font-size:11px;line-height:23px}
.mini-bag .info b{font-size:12px}
.mini-bag .total{position:absolute;left:12px;right:12px;top:170px;border-top:1px solid var(--line);padding-top:14px;display:flex;justify-content:space-between;align-items:center;font-size:11px}
.mini-bag .total b{font-size:22px;margin-right:22px}
.mini-btn{position:absolute;top:223px;height:32px;width:96px;background:var(--ink);color:var(--paper);font-size:12px;font-weight:600;display:flex;align-items:center;justify-content:center}
.cat-nav{top:132px;font-size:13px}
.promo-line{left:153px;top:168px;font-family:"Great Vibes",cursive;font-size:66px;color:var(--ink);white-space:nowrap}
.crumb{left:52px;top:280px;font-size:24px}
.crumb b{font-weight:600}
.photo{background:linear-gradient(180deg,var(--photo-a),var(--photo-b))}
.main-photo{left:52px;top:345px;width:392px;height:806px}
.thumb-img{left:471px;width:110px;height:181px}
.caret{left:526px;font-size:20px}
.title{left:646px;top:338px;font-size:27px;font-weight:700}
.price{left:652px;top:396px;font-size:30px;font-weight:700}
.ref{left:1020px;top:406px;font-size:18px}
.size{top:458px;width:77px;height:57px;background:var(--grey);color:var(--paper);font-size:30px;font-weight:700;display:flex;align-items:center;justify-content:center}
.size.active{background:var(--ink)}
.swatch{top:553px;width:77px;height:55px}
.add{left:654px;top:655px;width:178px;height:55px;background:var(--ink);color:var(--paper);font-size:22px;display:flex;align-items:center;justify-content:center}
.tabs{left:654px;top:762px;width:461px;height:56px;border-bottom:1px solid var(--line)}
.tab{position:absolute;top:0;height:56px;display:flex;align-items:center;font-size:21px}
.tab.active{left:0;width:182px;justify-content:center;border:1px solid var(--line);border-bottom:1px solid var(--paper);background:var(--paper)}
.desc{left:652px;top:852px;width:447px;font-size:20px;line-height:27px;font-weight:400}
.desc p{margin-bottom:27px;text-align:justify}
.desc p.plain{text-align:left}
.share{left:52px;top:1176px;font-size:24px}
.dot{width:34px;height:34px;border-radius:50%;background:var(--ink)}
.rule{left:20px;width:1100px;height:1px;background:var(--line)}
.section-title{left:0;width:1140px;top:1254px;text-align:center;font-size:38px;font-weight:300}
.product{top:1340px;height:330px}
.p-name{top:1683px;font-size:15px;font-weight:700;text-align:center}
.p-price{top:1707px;font-size:13px;text-align:center}
.promo{top:1756px;width:539px;height:257px;background:var(--promo-a);color:var(--paper);overflow:hidden}
.promo .figure{position:absolute;left:140px;top:0;width:260px;height:257px;background:linear-gradient(180deg,var(--promo-b),var(--promo-a))}
.promo .t{position:absolute;font-weight:600}
.footer{left:0;top:2035px;width:1200px;height:327px;background:var(--ink);color:var(--paper)}
.footer h4{position:absolute;top:38px;font-size:18px;font-weight:700}
.footer .addr{position:absolute;left:52px;top:82px;font-size:17px;font-weight:600;line-height:24px}
.footer .handle{position:absolute;left:517px;font-size:14px;display:flex;align-items:center}
.footer .fdot{position:absolute;left:440px;width:28px;height:28px;border-radius:50%;background:var(--paper)}
</style>
</head>
<body>
<header class="abs header">
  <div class="abs brand"><span class="brand-dot"></span>LUSHLINE</div>
  <span class="abs top-link" style="left:465px">STANDARD</span>
  <span class="abs top-link" style="left:595px">PLUS SIZE</span>
  <div class="abs search">search item</div>
  <span class="abs top-link" style="left:960px">LOGIN</span>
  <div class="abs bag">BAG
    <svg width="16" height="18" viewBox="0 0 16 18"><rect x="1" y="6" width="14" height="11" fill="#bbb"/><path d="M4 6V4a4 4 0 0 1 8 0v2" stroke="#bbb" stroke-width="2" fill="none"/></svg>
  </div>
</header>

<aside class="abs mini-bag">
  <div class="thumb" role="img" aria-label="Fringe black chemise product thumbnail"></div>
  <div class="info"><b>Fringe Black Chemise</b><br>Size: L<br>Color: Black<br>Price: $25.00<br>Quantity: 1</div>
  <div class="total"><span>Total items:</span><b>$25.00</b></div>
  <div class="mini-btn" style="left:12px">View Bag</div>
  <div class="mini-btn" style="left:124px">Checkout</div>
</aside>

<nav>
  <span class="abs cat-nav" style="left:60px">LINGERIE</span>
  <span class="abs cat-nav" style="left:170px">COSTUMES</span>
  <span class="abs cat-nav" style="left:298px">PANTIES</span>
  <span class="abs cat-nav" style="left:408px">DRESSES</span>
  <span class="abs cat-nav" style="left:523px">SLEEPWEAR</span>
  <span class="abs cat-nav" style="left:655px">HOSIERY</span>
  <span class="abs cat-nav" style="left:753px">ACCESORIES</span>
  <span class="abs cat-nav" style="left:884px">PVC</span>
</nav>

<div class="abs promo-line">Free Valentine’s Day Shipping Available</div>
<div class="abs crumb">HOME/<b>CHEMISE</b></div>

<div class="abs main-photo photo" role="img" aria-label="Model wearing the fringe black chemise and stockings"></div>
<span class="abs caret" style="top:310px">^</span>
<div class="abs thumb-img photo" style="top:345px" role="img" aria-label="Chemise view, front"></div>
<div class="abs thumb-img photo" style="top:554px" role="img" aria-label="Chemise view, side"></div>
<div class="abs thumb-img photo" style="top:762px" role="img" aria-label="Chemise view, angled"></div>
<div class="abs thumb-img photo" style="top:970px" role="img" aria-label="Chemise view, back"></div>
<span class="abs caret" style="top:1158px;font-size:16px">v</span>

<h1 class="abs title">Fringe Black Chemise</h1>
<div class="abs price">$25.00</div>
<div class="abs ref">ref: 029385</div>

<div class="abs size" style="left:655px">S</div>
<div class="abs size" style="left:746px">M</div>
<div class="abs size active" style="left:839px">L</div>
<div class="abs size" style="left:934px">XL</div>
<div class="abs size" style="left:1025px">XXL</div>

<div class="abs swatch" style="left:655px;background:var(--red)"></div>
<div class="abs swatch" style="left:746px;background:var(--blue)"></div>
<div class="abs swatch" style="left:839px;background:var(--paper);border:1px solid var(--grey)"></div>
<div class="abs swatch" style="left:934px;background:#000"></div>
<div class="abs swatch" style="left:1025px;background:var(--peach)"></div>

<div class="abs add">ADD TO BAG</div>

<div class="abs tabs">
  <div class="tab active">DESCRIPTION</div>
  <div class="tab" style="left:214px">SHIPPING</div>
  <div class="tab" style="left:362px">SIZING</div>
</div>

<div class="abs desc">
  <p>This sexy two-piece sheer lace and net babydoll includes the babydoll that features ribbon hemming, adjustable shoulder straps and back ties, and the matching g-string.</p>
  <p class="plain">Composition: 82% Polyester, 18% Elastane<br>Washing: Machine wash cold, gentle cycle with like colours<br>Made in: Australia</p>
  <p class="plain">Model is wearing size Small</p>
</div>

<div class="abs share">Share me</div>
<div class="abs dot" style="left:230px;top:1176px" aria-label="Share on Chirpline"></div>
<div class="abs dot" style="left:323px;top:1176px" aria-label="Share on Snapframe"></div>
<div class="abs dot" style="left:400px;top:1176px" aria-label="Share on Friendbook"></div>

<div class="abs rule" style="top:1249px"></div>
<h2 class="abs section-title">Popular Products</h2>
<div class="abs rule" style="top:1310px"></div>

<div class="abs product photo" style="left:52px;width:203px" role="img" aria-label="Model in black sheer babydoll"></div>
<div class="abs product photo" style="left:272px;width:204px" role="img" aria-label="Model in white babydoll with stockings"></div>
<div class="abs product photo" style="left:496px;width:205px" role="img" aria-label="Model in black lace high-waist set"></div>
<div class="abs product photo" style="left:718px;width:203px" role="img" aria-label="Model in white corset babydoll"></div>
<div class="abs product photo" style="left:942px;width:205px" role="img" aria-label="Model in black bustier babydoll"></div>

<div class="abs p-name" style="left:52px;width:203px">Babydoll</div><div class="abs p-price" style="left:52px;width:203px">$25.00</div>
<div class="abs p-name" style="left:272px;width:204px">Babydoll</div><div class="abs p-price" style="left:272px;width:204px">$25.00</div>
<div class="abs p-name" style="left:496px;width:205px">Babydoll</div><div class="abs p-price" style="left:496px;width:205px">$25.00</div>
<div class="abs p-name" style="left:718px;width:203px">Babydoll</div><div class="abs p-price" style="left:718px;width:203px">$25.00</div>
<div class="abs p-name" style="left:942px;width:205px">Babydoll</div><div class="abs p-price" style="left:942px;width:205px">$25.00</div>

<section class="abs promo" style="left:50px;background:#141414">
  <div class="figure" style="left:120px;background:linear-gradient(180deg,#5a4a44,#1a1a1a)" role="img" aria-label="Model in lace bodysuit and jacket"></div>
  <div class="t" style="left:27px;top:25px;font-size:40px;font-weight:400;line-height:52px">FREE<br><b>10%<br>OFF</b></div>
  <div class="t" style="left:328px;top:28px;font-size:40px;font-weight:700">CVNM10</div>
  <div class="t" style="left:10px;top:212px;font-size:22px">Coupon code applies to items more than $30.</div>
</section>

<section class="abs promo" style="left:610px">
  <div class="figure" role="img" aria-label="Model in blue corset"></div>
  <div class="t" style="left:10px;top:32px;font-size:34px;line-height:38px"><b>BUY ONE</b><br><span style="font-weight:400">GET ONE</span></div>
  <div class="t" style="left:350px;top:30px;font-size:80px;font-weight:700">50%</div>
  <div class="t" style="left:462px;top:118px;font-size:24px;font-weight:400">OFF</div>
  <div class="t" style="left:427px;top:212px;font-size:17px;text-decoration:underline">SHOP NOW</div>
</section>

<footer class="abs footer">
  <h4 style="left:52px">Address:</h4>
  <div class="addr">48 Orchard Lane East<br>Northbay<br>ON, Canada<br><br>1-800-LUSH-LINE<br>(1-800-587-4546)</div>
  <h4 style="left:447px">Follow us</h4>
  <span class="fdot" style="top:80px"></span><span class="handle" style="top:86px">@lushline</span>
  <span class="fdot" style="top:133px"></span><span class="handle" style="top:139px">photos.lushline.shop</span>
  <span class="fdot" style="top:186px"></span><span class="handle" style="top:192px">friends.lushline.shop</span>
  <h4 style="left:879px">Contact us</h4>
</footer>
</body>
</html>
```